Health & Wellness Contest - The Bright Path Sprint

We need a postcard design that is professional and grabs the attention of people who see it. The postcard will be left in fitness centers and posted on social media. The front of the card MUST look amazing - make potential participants want to pick it up and find out more information; the back of the card will have the contest details. The goal is to have people sign up for a 90 day fitness program, and most of the marketing will be with this postcard.

Target Market(s)

People that are thinking about beginning a health regiment; people who are already used to exercising and are willing to try a new supplement

Industry/Entity Type

Health And Wellness

Colors

Designer to choose colors to be used in the design.

Requirements
Must have
• Front Cover -- Must have the phrase "The Bright Path Sprint" and must have "$2,500 Grand Prize"; and must have "BrightPathSprint.com"
Nice to have
• Design on Front; Details on Back; appeal to both men and women

```html
<!DOCTYPE html>
<html lang="en">
<head>
<meta charset="utf-8">
<title>The Bright Path Sprint — Postcard</title>
<link rel="stylesheet" href="https://fonts.googleapis.com/css2?family=Marcellus&family=Source+Sans+3:wght@400;600;700&display=swap">
<style>
  :root {
    --teal: #1aa6bd;
    --teal-light: #2fc0d6;
    --teal-text: #1796ad;
    --gold: #f0ac1c;
    --gold-deep: #e39a0c;
    --tick: #f3c23a;
    --white: #ffffff;
    --page: #e9eaec;
    --photo-light: #f4efe8;
    --photo-mid: #e3d2bd;
    --photo-floor: #c99a68;
    --body-light: #5cc6d6;
    --body-tone: #c89a7c;
  }
  * { margin: 0; padding: 0; box-sizing: border-box; }
  html, body { width: 1200px; height: 960px; overflow: hidden; background: var(--page); }

  .postcard {
    position: absolute;
    width: 1050px; height: 700px;
    overflow: hidden;
    transform: scale(0.657);
    transform-origin: 0 0;
    box-shadow: 0 10px 30px rgba(0,0,0,.18);
    background: var(--white);
    font-family: "Source Sans 3", sans-serif;
    color: var(--white);
  }
  .postcard-front { left: 450px; top: 15px; }
  .postcard-back { left: 60px; top: 485px; }
  .postcard-shapes { position: absolute; inset: 0; }

  /* Front */
  .title { position: absolute; left: 40px; top: 34px; width: 500px; font-family: "Marcellus", serif; font-weight: 400; line-height: 1; }
  .title-lead { display: block; font-size: 46px; letter-spacing: .5px; }
  .title-main { display: block; font-size: 68px; margin-top: 14px; letter-spacing: 1px; }
  .mission { position: absolute; left: 30px; top: 212px; width: 470px; text-align: center; font-size: 18px; line-height: 1.25; }
  .invite { position: absolute; left: 20px; top: 268px; width: 500px; text-align: center; font-size: 21px; line-height: 1.2; color: var(--teal-text); }
  .benefits { position: absolute; top: 392px; list-style: none; font-size: 17px; }
  .benefits li { display: flex; align-items: center; gap: 9px; height: 27px; }
  .benefits-left { left: 28px; }
  .benefits-right { left: 272px; top: 404px; }
  .tick { width: 15px; height: 15px; flex: none; }
  .deadline { position: absolute; left: 48px; top: 560px; font-size: 22px; }
  .prize { position: absolute; width: 136px; text-align: center; line-height: 1; }
  .prize-label { display: block; font-size: 17px; }
  .prize-amount { display: block; font-size: 25px; font-weight: 600; margin-top: 8px; }
  .postcard-front .prize { left: 722px; top: 563px; }
  .site { position: absolute; left: 92px; top: 640px; font-size: 18px; }
  .site strong { font-weight: 700; }

  /* Back */
  .back-title { position: absolute; left: 50px; top: 30px; font-family: "Marcellus", serif; font-weight: 400; line-height: 1; }
  .back-title .title-lead { font-size: 42px; }
  .back-title .title-main { font-size: 62px; margin-top: 8px; }
  .back-mission { position: absolute; left: 50px; top: 168px; width: 420px; font-size: 17px; line-height: 1.25; text-align: center; }
  .back-deadline { position: absolute; left: 120px; top: 236px; font-size: 22px; line-height: 1.2; }
  .postcard-back .prize { left: 452px; top: 94px; }
  .sign-up { position: absolute; left: 110px; top: 462px; font-family: "Marcellus", serif; font-size: 66px; line-height: 1; }
  .back-site { position: absolute; left: 0; top: 568px; width: 790px; text-align: center; font-size: 30px; color: var(--teal-text); }
  .back-site strong { font-weight: 700; }
  .back-contact { position: absolute; left: 0; top: 622px; width: 800px; text-align: center; font-size: 19px; line-height: 1.3; }
</style>
</head>
<body>

<section class="postcard postcard-front">
  <svg class="postcard-shapes" width="1050" height="700" viewBox="0 0 1050 700">
    <defs>
      <linearGradient id="photoTone" x1="0" y1="0" x2="0" y2="1">
        <stop offset="0" stop-color="var(--photo-light)"/>
        <stop offset="0.6" stop-color="var(--photo-mid)"/>
        <stop offset="1" stop-color="var(--photo-floor)"/>
      </linearGradient>
      <clipPath id="frontPanelClip">
        <path d="M0,0 H585 C525,250 465,480 445,700 H0 Z"/>
      </clipPath>
    </defs>
    <g role="img" aria-label="Photo of a smiling woman in white exercise clothes crouching on a glass bathroom scale">
      <rect width="1050" height="700" fill="url(#photoTone)"/>
    </g>
    <path d="M0,0 H612 C550,250 492,480 472,700 H0 Z" fill="var(--white)"/>
    <path d="M630,0 C566,250 508,480 488,700" fill="none" stroke="var(--gold)" stroke-width="16"/>
    <g clip-path="url(#frontPanelClip)">
      <rect width="1050" height="700" fill="var(--teal)"/>
      <rect y="262" width="1050" height="112" fill="var(--white)"/>
      <rect y="374" width="1050" height="326" fill="var(--teal-light)"/>
    </g>
    <line x1="60" y1="195" x2="470" y2="195" stroke="var(--white)" stroke-width="2"/>
    <circle cx="265" cy="186" r="3" fill="var(--white)"/>
    <rect x="18" y="548" width="780" height="60" rx="30" fill="var(--gold)"/>
    <circle cx="790" cy="590" r="84" fill="var(--white)"/>
    <circle cx="790" cy="590" r="80" fill="var(--gold)" stroke="var(--white)" stroke-width="4" stroke-dasharray="4 4"/>
    <circle cx="790" cy="590" r="68" fill="var(--gold-deep)" stroke="var(--white)" stroke-width="2.5"/>
  </svg>

  <h1 class="title"><span class="title-lead">The Bright Path</span><span class="title-main">SPRINT</span></h1>
  <p class="mission">The Bright Path Sprint has one mission<br>to help people be a better version of themselves.</p>
  <p class="invite">Join us in the Bright Path Sprint<br>and experience some of the benefits that<br>countless others have seen:</p>

  <ul class="benefits benefits-left">
    <li><svg class="tick" viewBox="0 0 16 16"><circle cx="8" cy="8" r="7" fill="none" stroke="var(--tick)" stroke-width="1.6"/><path d="M4.5 8.2l2.3 2.3 4.7-4.8" fill="none" stroke="var(--tick)" stroke-width="1.8"/></svg>Better health</li>
    <li><svg class="tick" viewBox="0 0 16 16"><circle cx="8" cy="8" r="7" fill="none" stroke="var(--tick)" stroke-width="1.6"/><path d="M4.5 8.2l2.3 2.3 4.7-4.8" fill="none" stroke="var(--tick)" stroke-width="1.8"/></svg>Appetite suppression</li>
    <li><svg class="tick" viewBox="0 0 16 16"><circle cx="8" cy="8" r="7" fill="none" stroke="var(--tick)" stroke-width="1.6"/><path d="M4.5 8.2l2.3 2.3 4.7-4.8" fill="none" stroke="var(--tick)" stroke-width="1.8"/></svg>Better energy</li>
    <li><svg class="tick" viewBox="0 0 16 16"><circle cx="8" cy="8" r="7" fill="none" stroke="var(--tick)" stroke-width="1.6"/><path d="M4.5 8.2l2.3 2.3 4.7-4.8" fill="none" stroke="var(--tick)" stroke-width="1.8"/></svg>Fat Loss</li>
    <li><svg class="tick" viewBox="0 0 16 16"><circle cx="8" cy="8" r="7" fill="none" stroke="var(--tick)" stroke-width="1.6"/><path d="M4.5 8.2l2.3 2.3 4.7-4.8" fill="none" stroke="var(--tick)" stroke-width="1.8"/></svg>Better focus</li>
  </ul>
  <ul class="benefits benefits-right">
    <li><svg class="tick" viewBox="0 0 16 16"><circle cx="8" cy="8" r="7" fill="none" stroke="var(--tick)" stroke-width="1.6"/><path d="M4.5 8.2l2.3 2.3 4.7-4.8" fill="none" stroke="var(--tick)" stroke-width="1.8"/></svg>Increased awareness</li>
    <li><svg class="tick" viewBox="0 0 16 16"><circle cx="8" cy="8" r="7" fill="none" stroke="var(--tick)" stroke-width="1.6"/><path d="M4.5 8.2l2.3 2.3 4.7-4.8" fill="none" stroke="var(--tick)" stroke-width="1.8"/></svg>Better mood</li>
    <li><svg class="tick" viewBox="0 0 16 16"><circle cx="8" cy="8" r="7" fill="none" stroke="var(--tick)" stroke-width="1.6"/><path d="M4.5 8.2l2.3 2.3 4.7-4.8" fill="none" stroke="var(--tick)" stroke-width="1.8"/></svg>Muscle preservation</li>
    <li><svg class="tick" viewBox="0 0 16 16"><circle cx="8" cy="8" r="7" fill="none" stroke="var(--tick)" stroke-width="1.6"/><path d="M4.5 8.2l2.3 2.3 4.7-4.8" fill="none" stroke="var(--tick)" stroke-width="1.8"/></svg>Better sleep</li>
    <li><svg class="tick" viewBox="0 0 16 16"><circle cx="8" cy="8" r="7" fill="none" stroke="var(--tick)" stroke-width="1.6"/><path d="M4.5 8.2l2.3 2.3 4.7-4.8" fill="none" stroke="var(--tick)" stroke-width="1.8"/></svg>And much more...</li>
  </ul>

  <p class="deadline">Challenge Deadline: Register by October 31, 2017.</p>
  <p class="prize"><span class="prize-label">Grand Prize</span><span class="prize-amount">$2,500.00</span></p>
  <p class="site">www.<strong>BrightPathSprint</strong>.com</p>
</section>

<section class="postcard postcard-back">
  <svg class="postcard-shapes" width="1050" height="700" viewBox="0 0 1050 700">
    <defs>
      <linearGradient id="bodyTone" x1="0" y1="0" x2="1" y2="0">
        <stop offset="0" stop-color="var(--body-light)"/>
        <stop offset="0.35" stop-color="var(--body-tone)"/>
        <stop offset="0.7" stop-color="var(--body-light)"/>
        <stop offset="1" stop-color="var(--body-tone)"/>
      </linearGradient>
      <clipPath id="backPanelClip">
        <path d="M0,0 H600 C680,250 760,500 830,700 H0 Z"/>
      </clipPath>
    </defs>
    <path d="M625,0 C705,250 785,500 855,700" fill="none" stroke="var(--gold)" stroke-width="16"/>
    <g clip-path="url(#backPanelClip)">
      <rect width="1050" height="700" fill="var(--teal)"/>
      <g role="img" aria-label="Photo of a fit man and woman showing toned midsections">
        <rect y="300" width="1050" height="260" fill="url(#bodyTone)"/>
      </g>
      <rect y="555" width="1050" height="60" fill="var(--white)"/>
    </g>
    <line x1="70" y1="158" x2="450" y2="158" stroke="var(--white)" stroke-width="2"/>
    <circle cx="260" cy="150" r="3" fill="var(--white)"/>
    <rect x="80" y="226" width="440" height="80" rx="40" fill="var(--gold)"/>
    <circle cx="520" cy="140" r="84" fill="var(--white)"/>
    <circle cx="520" cy="140" r="80" fill="var(--gold)" stroke="var(--white)" stroke-width="4" stroke-dasharray="4 4"/>
    <circle cx="520" cy="140" r="68" fill="var(--gold-deep)" stroke="var(--white)" stroke-width="2.5"/>
  </svg>

  <h2 class="back-title"><span class="title-lead">The Bright Path</span><span class="title-main">SPRINT</span></h2>
  <p class="back-mission">The Bright Path Sprint has one mission<br>to help people be a better version of themselves.</p>
  <p class="back-deadline">Challenge Deadline:<br>Register by October 31, 2017.</p>
  <p class="prize"><span class="prize-label">Grand Prize</span><span class="prize-amount">$2,500.00</span></p>
  <p class="sign-up">sign up</p>
  <p class="back-site">www.<strong>BrightPathSprint</strong>.com</p>
  <p class="back-contact">For Challenge details, email one of our sponsors at<br>info@HarborlineGroup.org</p>
</section>

</body>
</html>
```